Web Site Design for a Finance (lending) Company

We are opening a new subsidiary that focuses on lending money in the real estate industry. We need a web site designed to represent the business.

The business is lending money to real estate investors. A typical client/borrower will be looking to borrow money to buy a house, renovate it and then sell it at a profit, all within 12 months or less.

Company name is Brevand Finance. Our logo is attached.

Attached is a general outline for the web site. We're working on writing more text for each page but this should give you enough to get started with some ideas.

Competitor web site that I like a lot (as an example): https://quorvelfunding.com/. Many of the general items on this site match what we will need (description of loan programs, FAQ)

Target Market(s)

Real estate investors (generally individuals or small companies with just a few people) who are buying homes, renovating them and then selling them at a profit.

Industry/Entity Type

Finance

Coding

Coded - Design and coding required

Number of Pages Required

5+ page

Colors

Designer to choose colors to be used in the design.

Requirements
Must have
• Minimalist design. Clean lines without too much clutter. Some stock photography is ok but the photos should not be distracting. They should almost fade in to the background so that user can focus on the key information about what our company does instead. We are a finance company, not a design company, so the information about our products will be more interesting to site visitors than the art.
• Some minimalist examples from Snapboard:
• https://www.snapboard-example.com/explore/minimalist-web-design/
Nice to have
• If you search in seekly for "hard money lenders" you will find many examples of web sites from our competition. I have provided a link above to competitor web site that I like a lot.
• I have attached our logo in EPS format. Logo is green. Web site doesn't have to be green but it should be of a color that will work well with the logo.

```html
<!DOCTYPE html>
<html lang="en">
<head>
<meta charset="utf-8">
<title>Brevand Finance</title>
<link href="https://fonts.googleapis.com/css2?family=Open+Sans:wght@400;600;700&family=Roboto:wght@400;500;700&display=swap" rel="stylesheet">
<style>
:root{
  --green:#1e6b4e;
  --green-dark:#14523b;
  --green-band:#2a6f55;
  --ink:#2b2b2b;
  --muted:#7a7a7a;
  --light:#f1f2f2;
  --line:#dcdcdc;
  --footer-bar:#3b3d3f;
}
*{box-sizing:border-box;margin:0;padding:0}
html,body{width:1200px;height:3044px;overflow:hidden}
body{font-family:"Open Sans",Arial,sans-serif;color:var(--ink);background:#fff;position:relative}
.section-title{font-family:"Roboto",Arial,sans-serif;font-weight:700;font-size:26px;color:var(--green);text-align:center;letter-spacing:.5px}
.title-rule{width:60px;height:3px;background:var(--green);margin:14px auto 18px}
.lead{font-size:14px;line-height:24px;color:var(--muted);text-align:center;width:900px;margin:0 auto}

/* header */
.site-header{position:absolute;top:0;left:0;width:1200px;height:108px;background:#fff}
.brand{position:absolute;left:88px;top:22px;display:flex;align-items:center;gap:12px}
.brand-square{width:22px;height:22px;background:var(--green)}
.brand-name{font-family:"Roboto",Arial,sans-serif;font-weight:700;font-size:30px;color:var(--green);line-height:1}
.live-chat{position:absolute;right:70px;top:0;width:130px;height:34px;background:var(--green);color:#fff;font-size:13px;font-weight:700;display:flex;align-items:center;justify-content:center;gap:8px;border-radius:0 0 6px 6px}
.main-nav{position:absolute;right:88px;top:58px;display:flex;gap:42px;font-family:"Roboto",Arial,sans-serif;font-size:14px;font-weight:500;color:var(--ink)}
.main-nav .active{color:var(--green);border-bottom:3px solid var(--green);padding-bottom:12px}

/* hero */
.hero{position:absolute;top:108px;left:0;width:1200px;height:492px;background:linear-gradient(180deg,#c9d7e2 0%,#b9c6cc 38%,#a79a86 58%,#6d8a4e 78%,#557a3c 100%)}
.hero-card{position:absolute;left:88px;top:168px;width:300px;padding:22px 26px;background:rgba(30,40,35,.72);color:#fff}
.hero-card h1{font-family:"Roboto",Arial,sans-serif;font-size:34px;font-weight:700;letter-spacing:1px}
.hero-card p{font-size:12px;line-height:18px;margin-top:10px;color:#e6e6e6}
.dots{position:absolute;left:0;right:0;bottom:14px;display:flex;justify-content:center;gap:8px}
.dots span{width:10px;height:10px;border-radius:50%;background:#fff;opacity:.55}
.dots span.on{opacity:1;background:var(--green)}

/* features */
.features{position:absolute;top:600px;left:0;width:1200px;height:312px;display:flex}
.feature{width:400px;height:312px;background:var(--light);text-align:center;padding-top:40px}
.feature.mid{background:#fff}
.feature h3{font-family:"Roboto",Arial,sans-serif;font-size:18px;font-weight:700;margin-top:14px;color:var(--ink)}
.feature p{font-size:12px;line-height:20px;color:var(--muted);width:290px;margin:12px auto 20px}
.btn-outline{display:inline-block;border:1px solid #9a9a9a;padding:8px 16px;font-size:11px;font-weight:700;color:var(--ink)}

/* welcome */
.welcome{position:absolute;top:966px;left:0;width:1200px}
.about{position:absolute;top:1140px;left:88px;width:1024px;height:320px;display:flex;gap:40px}
.about-photo{width:420px;height:320px;background:linear-gradient(160deg,#e8e4de 0%,#c8a88a 45%,#9e6f55 75%,#7a8a6a 100%)}
.about-body h2{font-family:"Roboto",Arial,sans-serif;font-size:18px;font-weight:700;color:var(--ink);padding-top:8px}
.about-body .rule{width:50px;height:3px;background:var(--green);margin:12px 0 20px}
.checks{list-style:none}
.checks li{display:flex;gap:14px;font-size:11px;line-height:18px;color:#555;text-transform:uppercase;margin-bottom:18px;width:560px}
.checks svg{flex:none;margin-top:2px}

/* testimonials */
.testimonials{position:absolute;top:1540px;left:0;width:1200px;height:340px;background:linear-gradient(135deg,#1d5d45 0%,#2d7a5c 50%,#1a5240 100%);color:#fff;text-align:center;padding-top:34px}
.testimonials .section-title{color:#fff;font-size:22px}
.avatars{display:flex;justify-content:center;align-items:center;gap:10px;margin:26px 0 22px}
.avatar{width:70px;height:70px;border-radius:50%;border:3px solid #fff;background:linear-gradient(#c9b8a6,#8f7c6a)}
.avatar.big{width:92px;height:92px;background:linear-gradient(#d8c2ad,#9a7d66)}
.quote{position:relative;width:820px;margin:0 auto;font-size:13px;line-height:22px;color:#e8f1ed}
.quote .mark{position:absolute;font-family:Georgia,serif;font-size:46px;line-height:1;color:#fff}
.quote .open{left:-36px;top:-6px}
.quote .close{right:-36px;bottom:-22px}
.quote-name{font-family:"Roboto",Arial,sans-serif;font-weight:700;font-size:13px;margin-top:18px;letter-spacing:1px}

/* resources */
.resources{position:absolute;top:1926px;left:0;width:1200px}
.cards{display:flex;gap:46px;width:1024px;margin:26px auto 0}
.card{width:310px}
.card-photo{height:200px}
.card h4{font-family:"Roboto",Arial,sans-serif;font-size:16px;font-weight:700;color:var(--green);margin:14px 0 8px}
.card p{font-size:12px;line-height:20px;color:var(--muted)}

/* membership */
.membership{position:absolute;top:2456px;left:0;width:1200px;height:276px;background:var(--light);padding-top:40px}
.partners{display:flex;justify-content:center;align-items:center;gap:24px;margin-top:30px}
.partner{width:170px;height:96px;background:#fff;display:flex;align-items:center;justify-content:center}
.partner span{width:100px;height:22px;background:#cfd3d3;border-radius:3px}
.arrow{color:#9a9a9a;font-size:26px;width:30px;text-align:center}

/* footer */
.site-footer{position:absolute;top:2764px;left:0;width:1200px;height:216px}
.foot-brand{position:absolute;left:88px;top:30px;display:flex;align-items:center;gap:12px}
.foot-col{position:absolute;top:14px}
.foot-col h5{font-family:"Roboto",Arial,sans-serif;font-size:15px;font-weight:700;color:var(--ink);margin-bottom:14px}
.contact-list{list-style:none;font-size:12px;color:#555}
.contact-list li{display:flex;align-items:center;gap:10px;margin-bottom:10px}
.foot-col p{font-size:12px;line-height:18px;color:var(--muted);width:220px}
.email-field{width:220px;height:30px;border:1px solid var(--line);margin-top:12px;font-size:11px;color:#999;padding:7px 10px}
.btn-green{display:inline-block;background:var(--green);color:#fff;font-size:11px;font-weight:700;padding:8px 14px;margin-top:10px}
.socials{display:flex;gap:8px;margin-top:14px}
.socials span{width:30px;height:30px;border-radius:50%;border:1px solid #9a9a9a}
.foot-bar{position:absolute;top:2980px;left:0;width:1200px;height:64px;background:var(--footer-bar);color:#bbb;font-size:12px;display:flex;align-items:center;justify-content:center}
.to-top{position:absolute;right:40px;top:18px;width:28px;height:28px;background:#555}
</style>
</head>
<body>

<header class="site-header">
  <div class="brand"><span class="brand-square"></span><span class="brand-name">Brevand Finance</span></div>
  <div class="live-chat">
    <svg width="14" height="12" viewBox="0 0 14 12"><path d="M1 1h12v7H6l-3 3V8H1z" fill="#fff"/></svg>LIVE CHAT
  </div>
  <nav class="main-nav">
    <span class="active">HOME</span><span>ABOUT US</span><span>LOANS</span><span>RESOURCES</span><span>CONTACT US</span>
    <svg width="14" height="14" viewBox="0 0 14 14"><circle cx="6" cy="6" r="4.5" fill="none" stroke="#2b2b2b" stroke-width="1.6"/><path d="M9.5 9.5L13 13" stroke="#2b2b2b" stroke-width="1.6"/></svg>
  </nav>
</header>

<section class="hero" role="img" aria-label="Large family house with a green front lawn under a cloudy sky">
  <div class="hero-card">
    <h1>BREVAND FINANCE</h1>
    <p>Fast, flexible short term loans for investors who buy, renovate and sell homes within a year.</p>
  </div>
  <div class="dots"><span></span><span class="on"></span><span></span></div>
</section>

<section class="features">
  <div class="feature">
    <svg width="56" height="56" viewBox="0 0 56 56"><path d="M20 10h16l-4 8h-8z" fill="#1e6b4e"/><circle cx="28" cy="34" r="16" fill="#1e6b4e"/><text x="28" y="41" text-anchor="middle" font-family="Roboto,Arial,sans-serif" font-size="20" font-weight="700" fill="#fff">$</text></svg>
    <h3>BORROWERS</h3>
    <p>Short term funding for purchase and rehab projects with clear terms and quick answers on every deal.</p>
    <span class="btn-outline">READ MORE</span>
  </div>
  <div class="feature mid">
    <svg width="56" height="56" viewBox="0 0 56 56"><circle cx="28" cy="28" r="24" fill="none" stroke="#1e6b4e" stroke-width="4"/><text x="28" y="37" text-anchor="middle" font-family="Roboto,Arial,sans-serif" font-size="24" font-weight="700" fill="#1e6b4e">$</text></svg>
    <h3>INVESTORS</h3>
    <p>Earn steady returns backed by real estate, with loans secured by homes in active local markets.</p>
    <span class="btn-outline">READ MORE</span>
  </div>
  <div class="feature">
    <svg width="56" height="56" viewBox="0 0 56 56"><rect x="8" y="10" width="40" height="26" fill="none" stroke="#1e6b4e" stroke-width="3"/><path d="M14 30l9-9 7 5 10-10" fill="none" stroke="#1e6b4e" stroke-width="3"/><path d="M28 36v10M20 48h16" stroke="#1e6b4e" stroke-width="3"/></svg>
    <h3>RECENT PROJECTS</h3>
    <p>See homes our borrowers bought, renovated and sold with funding closed in days, not months.</p>
    <span class="btn-outline">READ MORE</span>
  </div>
</section>

<section class="welcome">
  <h2 class="section-title">WELCOME TO BREVAND FINANCE</h2>
  <div class="title-rule"></div>
  <p class="lead">We lend to real estate investors who buy homes, renovate them and sell them at a profit. Our loan programs are simple, our process is fast and our team knows the local market, so you can focus on the project while we handle the funding behind it.</p>
</section>

<section class="about">
  <div class="about-photo" role="img" aria-label="Small model house resting on a wooden table"></div>
  <div class="about-body">
    <h2>SED UT PERSPICIATIS UNDE OMNIS ISTE NATUS ERROR</h2>
    <div class="rule"></div>
    <ul class="checks">
      <li><svg width="14" height="14" viewBox="0 0 14 14"><path d="M2 7l3 3 7-7" fill="none" stroke="#1e6b4e" stroke-width="2"/></svg>Loans for purchase and renovation of single family homes</li>
      <li><svg width="14" height="14" viewBox="0 0 14 14"><path d="M2 7l3 3 7-7" fill="none" stroke="#1e6b4e" stroke-width="2"/></svg>Terms of twelve months or less with interest only payments and no penalty for early payoff on sale</li>
      <li><svg width="14" height="14" viewBox="0 0 14 14"><path d="M2 7l3 3 7-7" fill="none" stroke="#1e6b4e" stroke-width="2"/></svg>Quick approval based on the property and your plan</li>
      <li><svg width="14" height="14" viewBox="0 0 14 14"><path d="M2 7l3 3 7-7" fill="none" stroke="#1e6b4e" stroke-width="2"/></svg>Rehab funds released in draws as each stage of work is finished and checked on site</li>
      <li><svg width="14" height="14" viewBox="0 0 14 14"><path d="M2 7l3 3 7-7" fill="none" stroke="#1e6b4e" stroke-width="2"/></svg>Direct lender with local staff</li>
    </ul>
  </div>
</section>

<section class="testimonials" role="img" aria-label="Green tinted background photo of a business meeting">
  <h2 class="section-title">OUR TESTIMONIALS</h2>
  <div class="avatars">
    <div class="avatar" role="img" aria-label="Client portrait"></div>
    <div class="avatar big" role="img" aria-label="Client portrait"></div>
    <div class="avatar" role="img" aria-label="Client portrait"></div>
  </div>
  <p class="quote"><span class="mark open">&ldquo;</span>The team closed our loan in under two weeks and the draw process kept our renovation moving. We sold the house ahead of schedule and are already planning the next one together.<span class="mark close">&rdquo;</span></p>
  <p class="quote-name">DANA WHITLOW</p>
</section>

<section class="resources">
  <h2 class="section-title">INVESTOR RESOURCES</h2>
  <div class="title-rule"></div>
  <p class="lead">Guides, checklists and market notes to help you plan each project and apply with confidence.</p>
  <div class="cards">
    <div class="card">
      <div class="card-photo" role="img" aria-label="Business people reviewing papers in an office" style="background:linear-gradient(150deg,#d9dcdf,#8b8f93 60%,#5b5f63)"></div>
      <h4>Sed ut perspiciatis unde</h4>
      <p>How to estimate repair costs and build a budget that lenders trust for your next flip.</p>
    </div>
    <div class="card">
      <div class="card-photo" role="img" aria-label="Agents talking in front of a house under construction" style="background:linear-gradient(150deg,#cfe0ea,#b9a48a 55%,#7f6b55)"></div>
      <h4>Sed ut perspiciatis unde</h4>
      <p>What we look for in a deal and how to prepare your plan before you submit an application.</p>
    </div>
    <div class="card">
      <div class="card-photo" role="img" aria-label="Agent meeting buyers outside a brick home" style="background:linear-gradient(150deg,#dfe6ea,#a8876b 55%,#5f6a52)"></div>
      <h4>Sed ut perspiciatis unde</h4>
      <p>Timing your sale, pricing the finished home and paying off the loan on schedule.</p>
    </div>
  </div>
</section>

<section class="membership">
  <h2 class="section-title" style="font-size:22px">OUR MEMBERSHIP</h2>
  <div class="title-rule"></div>
  <p class="lead">We are proud members of local lending and real estate investor groups.</p>
  <div class="partners">
    <span class="arrow">&lsaquo;</span>
    <div class="partner"><span></span></div>
    <div class="partner"><span></span></div>
    <div class="partner"><span></span></div>
    <div class="partner"><span></span></div>
    <div class="partner"><span></span></div>
    <span class="arrow">&rsaquo;</span>
  </div>
</section>

<footer class="site-footer">
  <div class="foot-brand"><span class="brand-square"></span><span class="brand-name" style="font-size:28px">Brevand Finance</span></div>
  <div class="foot-col" style="left:390px">
    <h5>CONTACT US</h5>
    <ul class="contact-list">
      <li><svg width="12" height="12" viewBox="0 0 12 12"><path d="M2 1h3l1 3-2 1a7 7 0 003 3l1-2 3 1v3c-6 1-10-3-9-9z" fill="#1e6b4e"/></svg>(555) 014-2290 Office</li>
      <li><svg width="12" height="12" viewBox="0 0 12 12"><path d="M2 1h3l1 3-2 1a7 7 0 003 3l1-2 3 1v3c-6 1-10-3-9-9z" fill="#1e6b4e"/></svg>(555) 014-2291 Fax</li>
      <li><svg width="12" height="12" viewBox="0 0 12 12"><rect x="1" y="2.5" width="10" height="7" fill="none" stroke="#1e6b4e" stroke-width="1.4"/><path d="M1 3l5 4 5-4" fill="none" stroke="#1e6b4e" stroke-width="1.4"/></svg>hello@brevandfinance.com</li>
      <li><svg width="12" height="12" viewBox="0 0 12 12"><path d="M6 11S2 7 2 4.5a4 4 0 018 0C10 7 6 11 6 11z" fill="#1e6b4e"/><circle cx="6" cy="4.5" r="1.4" fill="#fff"/></svg>12 Linden Road, Suite 4</li>
    </ul>
  </div>
  <div class="foot-col" style="left:640px">
    <h5>NEWSLETTER</h5>
    <p>Get new loan programs and market notes in your inbox.</p>
    <div class="email-field">Email Address</div>
    <span class="btn-green">SUBSCRIBE</span>
  </div>
  <div class="foot-col" style="left:895px">
    <h5>FOLLOW US</h5>
    <p>Stay connected for project updates and news.</p>
    <div class="socials"><span></span><span></span><span></span><span></span><span></span></div>
  </div>
</footer>

<div class="foot-bar">&copy; Copyright 2017 Brevand Finance. All Rights Reserved.<span class="to-top"></span></div>

</body>
</html>
```